Fernvale Business Card Design

We are looking for a fresh business card design for our new logo. We would like a business card that is unique but friendly. We are in the window coverings business offering blinds, shutters and shades for homes.

Target Market(s)

Targeting the end-consumer

Industry/Entity Type

Business

Requirements
Must have
• Must have a dedicates space for a photo of our sales person. Must contain our new logo (attached).

```html
<!DOCTYPE html>
<html lang="en">
<head>
<meta charset="utf-8">
<title>Fernvale Business Card</title>
<link rel="stylesheet" href="https://fonts.googleapis.com/css2?family=Arimo:ital,wght@0,400;0,700;1,400&display=swap">
<style>
  :root {
    --green: #8dc63f;
    --grey: #666666;
    --text-grey: #5f5f5f;
    --white: #ffffff;
    --photo-top: #5a7a78;
    --photo-bottom: #1f3a3a;
  }
  html, body {
    margin: 0;
    padding: 0;
    width: 1200px;
    height: 1058px;
    overflow: hidden;
    background: var(--white);
    font-family: "Arimo", Arial, sans-serif;
  }
  .card {
    position: absolute;
    left: 306px;
    width: 530px;
    height: 334px;
    box-shadow: 18px 12px 16px rgba(0,0,0,0.45);
  }
  .card-front {
    top: 180px;
    background: var(--white);
    border: 1px solid #9a9a9a;
    box-sizing: border-box;
    border-radius: 40px 0 40px 0;
  }
  .card-back {
    top: 550px;
    background: var(--grey);
    border-radius: 0 40px 0 40px;
  }
  .photo {
    position: absolute;
    left: 41px;
    top: 39px;
    width: 130px;
    height: 163px;
    border-radius: 0 0 16px 0;
    background: linear-gradient(160deg, var(--photo-top), var(--photo-bottom));
    box-shadow: 6px 5px 0 #555555;
  }
  .details {
    position: absolute;
    right: 38px;
    text-align: right;
    color: var(--text-grey);
    margin: 0;
  }
  .employee-name {
    top: 32px;
    font-size: 21px;
    font-weight: 700;
    color: var(--green);
  }
  .employee-title {
    top: 58px;
    font-size: 16px;
  }
  .mobile {
    top: 79px;
    font-size: 16px;
  }
  .brand-name {
    top: 126px;
    font-size: 35px;
    color: var(--text-grey);
  }
  .website {
    top: 196px;
    font-size: 15px;
    font-style: italic;
    letter-spacing: 5px;
    margin-right: -5px;
    color: var(--green);
  }
  .phone {
    top: 264px;
    font-size: 16px;
  }
  .email {
    top: 285px;
    font-size: 16px;
  }
  .back-brand {
    position: absolute;
    left: 0;
    right: 0;
    top: 140px;
    text-align: center;
    font-size: 38px;
    color: var(--green);
    margin: 0;
  }
</style>
</head>
<body>
  <section class="card card-front">
    <div class="photo" role="img" aria-label="Portrait photo of the sales person"></div>
    <p class="details employee-name">employee name</p>
    <p class="details employee-title">employee title</p>
    <p class="details mobile">M + 0000 000000</p>
    <p class="details brand-name">Fernvale</p>
    <p class="details website">www.fernvale.com</p>
    <p class="details phone">Phone : 555.014.2280</p>
    <p class="details email">e-mail : name@fernvale.com</p>
  </section>
  <section class="card card-back">
    <p class="back-brand">Fernvale</p>
  </section>
</body>
</html>
```